Roofing Contractor business card redesign

I want to redesign my business card with a fresh, eye catching concept

Target Market(s)

Residential Roofing Clients, potential employees, and subcontractors.

Industry/Entity Type

Business

Colors

Designer to choose colors to be used in the design.

Requirements
Nice to have
• I just want something that's more pleasing to the eye. You can use a combination of either / or of my logos.

```html
<!DOCTYPE html>
<html lang="en">
<head>
<meta charset="utf-8">
<title>Brightline Builders – Business Card</title>
<link rel="stylesheet" href="https://fonts.googleapis.com/css2?family=Open+Sans:wght@400;600;700;800&display=swap">
<style>
  :root {
    --stage: #ecebe8;
    --card-white: #ffffff;
    --card-black: #2b2b2b;
    --brown: #4a1010;
    --orange: #e8711f;
    --ink: #3a2a2a;
    --logo-light: #ffffff;
  }
  * { margin: 0; padding: 0; box-sizing: border-box; }
  html, body {
    width: 1200px; height: 900px; overflow: hidden;
    background: var(--stage);
    font-family: "Open Sans", Arial, sans-serif;
  }
  .stage { position: relative; width: 1200px; height: 900px; }
  .card {
    position: absolute; width: 620px; height: 354px; left: 290px;
    border-radius: 4px; overflow: hidden;
    box-shadow: 0 6px 18px rgba(0,0,0,.18);
  }
  .card--back { top: 56px; background: var(--card-black); }
  .card--front { top: 466px; background: var(--card-white); }

  .brand { position: absolute; display: flex; align-items: center; gap: 14px; font-weight: 800; }
  .brand__dot { width: 46px; height: 46px; border-radius: 50%; flex: none; }
  .brand__name { line-height: 1.05; }
  .brand__name span { display: block; }
  .brand__main { font-size: 40px; letter-spacing: -0.5px; }
  .brand__sub { font-size: 22px; }

  .card--back .brand { left: 50%; top: 50%; transform: translate(-50%, -50%); color: var(--logo-light); }
  .card--back .brand__dot { background: var(--orange); }

  .card--front .brand { left: 318px; top: 118px; color: var(--brown); }
  .card--front .brand__main { font-size: 30px; }
  .card--front .brand__sub { font-size: 17px; }
  .card--front .brand__dot { width: 36px; height: 36px; background: var(--orange); }

  .deco { position: absolute; inset: 0; }

  .person { position: absolute; left: 74px; top: 20px; color: var(--ink); }
  .person__name { font-size: 17px; font-weight: 700; color: var(--brown); }
  .person__role { font-size: 12.5px; line-height: 1.35; }

  .address { position: absolute; left: 40px; top: 112px; font-size: 13px; line-height: 1.4; color: var(--ink); }

  .contacts { position: absolute; left: 40px; top: 164px; list-style: none; font-size: 13px; color: var(--ink); }
  .contacts li { display: flex; align-items: center; gap: 10px; height: 20px; }
  .contacts svg { width: 11px; height: 11px; fill: var(--brown); flex: none; }
</style>
</head>
<body>
<main class="stage">

  <section class="card card--back" aria-label="Card back">
    <div class="brand">
      <span class="brand__dot"></span>
      <div class="brand__name">
        <span class="brand__main">Brightline</span>
        <span class="brand__sub">Builders, Inc.</span>
      </div>
    </div>
  </section>

  <section class="card card--front" aria-label="Card front">
    <svg class="deco" viewBox="0 0 620 354" aria-hidden="true">
      <polygon points="0,0 48,0 30,44 0,44" fill="var(--orange)"/>
      <polygon points="52,0 66,0 48,44 34,44" fill="var(--brown)"/>
      <polygon points="0,258 300,258 284,290 0,290" fill="var(--brown)"/>
      <polygon points="312,276 620,276 620,322 294,322" fill="var(--orange)"/>
    </svg>

    <div class="person">
      <p class="person__name">Sam Porter</p>
      <p class="person__role">Keystone Certified Roof Inspector<br>Licensed Property Adjuster</p>
    </div>

    <p class="address">4180 Cedar Ridge Drive Suite 110<br>Plano, TX 75093</p>

    <ul class="contacts">
      <li><svg viewBox="0 0 12 12"><path d="M2.5 0.5l2 2-1 1.5c.7 1.6 2 2.9 3.5 3.5l1.5-1 2 2-1.5 2C4.5 10.5 1.5 7.5 0.5 2z"/></svg>(555) 210-4800</li>
      <li><svg viewBox="0 0 12 12"><path d="M3 0h6v12H3zM4 1.5v8h4v-8z"/></svg>(555) 318-2460</li>
      <li><svg viewBox="0 0 12 12"><path d="M0 2h12v8H0zM1 3l5 3.5L11 3z" fill-rule="evenodd"/></svg>sam@brightlinetx.com</li>
      <li><svg viewBox="0 0 12 12"><circle cx="6" cy="6" r="5.5"/></svg>BrightlineBuilders.com</li>
    </ul>

    <div class="brand">
      <span class="brand__dot"></span>
      <div class="brand__name">
        <span class="brand__main">Brightline</span>
        <span class="brand__sub">Builders, Inc.</span>
      </div>
    </div>
  </section>

</main>
</body>
</html>
```